Professional website for psychological services

Create a professional, easy to navigate website using soothing coastal images and incorporate company logo in design. Website is for a small private clinic that provides psychological services and must be appealing to professional men and women. A website I really like is www.veltoriparc.com I would love something like similar.

Target Market(s)

Professional men and women seeking psychological services

Industry/Entity Type

Mental Health

Number of Pages Required

5+ page

Requirements
Must have
• The website must incorporate the logo provided. The name of the company/website is Brimwell Harbor Renewal Aftercare. Colors must compliment the logo, must be coastal and soothing yet very professional. I would like a website like www.veltoriparc.com
• Pages will be:Home, Services, FAQ and Contact Us. The images included of the building and office are for the contact us page. Under the tab Servies: Individual Psychotherapy, Family Therapy, EMDR I will provide specific content for each.
Nice to have
• I want the website to be easy to navigate and the font easy to read. The writing on the logo is very light and I'm open to changing it slightly if it will be better aesthetically.
Should not have
• Please no pictures of any swimsuits, alcoholic beverages, etc. This is a professional psychological clinic.

```html
<!DOCTYPE html>
<html lang="en">
<head>
<meta charset="utf-8">
<title>Brimwell Harbor — Website Layout</title>
<link href="https://fonts.googleapis.com/css2?family=Arimo:wght@400;500&family=Open+Sans:wght@400&family=Great+Vibes&display=swap" rel="stylesheet">
<style>
:root{
  --cyan:#1fb5cf;
  --ink:#111;
  --field:#f1f1f1;
  --field-edge:#d6d6d6;
  --sand:#e4d4bf;
  --footer:#000;
  --sea-top:#5a7076;
  --sea-low:#475b61;
  --portrait-a:#6d8a66;
  --portrait-b:#4f6a4c;
}
*{box-sizing:border-box;margin:0;padding:0}
html,body{width:1200px;height:1200px;overflow:hidden}
body{position:relative;background:#fff;font-family:"Arimo",Arial,sans-serif;color:var(--ink)}
.abs{position:absolute}

.backdrop{left:0;top:0;width:1200px;height:1200px;
  background:linear-gradient(180deg,#5d7f7a 0%,#2f4c52 35%,#466a72 60%,#3b5960 100%)}
.backdrop-top{left:0;top:0;width:523px;height:49px;background:linear-gradient(90deg,#5f8078,#8aa58f 40%,#4b6b6a)}
.backdrop-low{left:569px;top:1070px;width:631px;height:130px;background:linear-gradient(180deg,#4b5f66 0%,#7a6a64 100%)}
.page-white{background:#fff}

.btn{display:flex;align-items:center;justify-content:center;border-radius:4px;font-family:"Arimo",sans-serif;box-shadow:0 1px 2px rgba(0,0,0,.25)}
.btn-solid{background:var(--cyan);color:#fff}
.btn-line{background:#fff;color:var(--cyan);border:2px solid var(--cyan)}

.brand{left:46px;width:523px;top:92px;text-align:center;color:var(--cyan);font-size:15px}
.brand-dot{display:inline-block;width:10px;height:10px;border-radius:50%;background:var(--cyan);margin-right:6px;vertical-align:1px}
.nav{top:142px;font-size:7px;color:#222}
.nav.active{color:var(--cyan)}

.photo-sea{background:linear-gradient(180deg,#6b8388 0%,#586f74 40%,#56646a 100%)}
.portrait{border-radius:50%;border:4px solid var(--cyan);background:linear-gradient(160deg,var(--portrait-a),var(--portrait-b))}
.room{background:linear-gradient(135deg,#8c7560,#6a5040)}
.garden{background:linear-gradient(160deg,#8aa6b6,#7c8f76)}
.thumb{top:318px;width:28px;height:28px}

.quote{left:226px;top:222px;width:170px;color:#fff;font-size:10px;line-height:12px}
.author{left:270px;top:259px;width:114px;text-align:right;color:#fff;font-family:"Great Vibes",cursive;font-size:16px}
.chev{color:var(--cyan);font-size:12px;top:191px}

.title{text-align:center;color:var(--ink);font-weight:400;letter-spacing:-.3px}
.about-copy{left:46px;width:523px;top:448px;text-align:center;font-family:"Open Sans",sans-serif;font-size:8.3px;line-height:17.5px;color:#222}

.services{overflow:hidden;background:linear-gradient(180deg,var(--sea-top) 0%,var(--sea-low) 70%,#5b7378 100%)}
.svc-title{color:#f2e6dc;text-align:center}
.svc-col{color:#fff;font-family:"Open Sans",sans-serif}
.svc-col h3{font-weight:400;font-family:"Open Sans",sans-serif}
.svc-col .more{color:#d8d0ca}

.field{background:var(--field);border:1px solid var(--field-edge);color:var(--cyan);display:flex;align-items:flex-start}
.info{color:var(--ink)}
.info .label{color:#444}

.newsletter{left:569px;top:954px;width:631px;height:69px;background:var(--sand)}
.footer{left:569px;top:1023px;width:631px;height:47px;background:var(--footer);color:#fff;font-size:10px}
.social{width:19px;height:19px;border-radius:50%;background:#2b6fb5;border:2px solid #8fb6e0}
</style>
</head>
<body>

<div class="abs backdrop" role="img" aria-label="Blurred coastal photograph behind the page layouts"></div>
<div class="abs backdrop-top" role="img" aria-label="Blurred coastal photograph"></div>

<div class="abs page-white" style="left:46px;top:49px;width:523px;height:1151px"></div>
<div class="abs page-white" style="left:523px;top:0;width:46px;height:49px"></div>

<div class="abs brand"><span class="brand-dot"></span>Brimwell Harbor Renewal Aftercare</div>
<div class="abs nav active" style="left:229px">Home</div>
<div class="abs nav" style="left:266px">Services</div>
<div class="abs nav" style="left:314px">FAQ</div>
<div class="abs nav" style="left:346px">Contact Us</div>

<div class="abs photo-sea" style="left:46px;top:162px;width:523px;height:208px" role="img" aria-label="Calm sea with distant hills at dusk"></div>
<div class="abs portrait" style="left:76px;top:187px;width:128px;height:128px" role="img" aria-label="Portrait photo of the clinician"></div>
<p class="abs quote">"Lorem ipsum dolor sit amet, consectetur adipiscing elit, sed do eiusmod tempor incididunt ut"</p>
<div class="abs author">Author's Name</div>
<div class="abs chev" style="left:396px">&#8249;</div>
<div class="abs chev" style="left:420px">&#8250;</div>
<div class="abs room" style="left:398px;top:208px;width:106px;height:102px" role="img" aria-label="Clinic office interior photo"></div>
<div class="abs garden" style="left:509px;top:208px;width:60px;height:102px" role="img" aria-label="Clinic building photo"></div>
<div class="abs thumb room" style="left:396px;border:2px solid var(--cyan)" role="img" aria-label="Office thumbnail"></div>
<div class="abs thumb garden" style="left:433px" role="img" aria-label="Building thumbnail"></div>
<div class="abs thumb" style="left:469px;background:linear-gradient(180deg,#3d8fd6,#2a6fb0)" role="img" aria-label="Sea thumbnail"></div>
<div class="abs thumb" style="left:505px;background:linear-gradient(180deg,#cfd6d8,#a8a89a)" role="img" aria-label="Garden thumbnail"></div>
<div class="abs thumb" style="left:541px;width:28px;background:linear-gradient(90deg,#e0ddd6,#8a7a6a)" role="img" aria-label="Sunset thumbnail"></div>
<svg class="abs" style="left:300px;top:332px" width="14" height="16" viewBox="0 0 14 16"><path d="M7 1v13M2 9l5 5 5-5" stroke="#fff" stroke-width="1.4" fill="none"/></svg>

<h2 class="abs title" style="left:46px;width:523px;top:411px;font-size:17px">ABOUT BRIMWELL</h2>
<p class="abs about-copy">Lorem ipsum dolor sit amet, consectetur adipiscing elit, sed do eiusmod tempor<br>incididunt ut labore et dolore magna aliqua. Ut enim ad minim veniam, quis nostrud<br>exercitation ullamco laboris nisi ut aliquip ex ea commodo consequat. Duis aute irure.</p>
<div class="abs btn btn-solid" style="left:222px;top:510px;width:75px;height:24px;font-size:8px">CONTACT US</div>
<div class="abs btn btn-line" style="left:318px;top:510px;width:75px;height:24px;font-size:8px">LEARN MORE</div>

<section class="abs services" style="left:46px;top:570px;width:523px;height:280px" role="img" aria-label="Coastal bay photo with islands and a sandy shore">
  <h2 class="abs svc-title" style="left:0;width:100%;top:53px;font-size:17px;font-weight:400">SERVICES</h2>
  <div class="abs svc-col" style="left:57px;top:86px;width:140px"><h3 style="font-size:12.5px">SPEAKING</h3><p style="font-size:8.3px;line-height:17.5px;margin-top:2px">Lorem ipsum dolor sit<br>amet, consectetur adipiscing<br>elit, sed do eiusmod tempor<br>incididunt ut <span class="more">learn more...</span></p></div>
  <div class="abs svc-col" style="left:204px;top:86px;width:140px"><h3 style="font-size:12.5px">TRAINING</h3><p style="font-size:8.3px;line-height:17.5px;margin-top:2px">Lorem ipsum dolor sit<br>amet, consectetur adipiscing<br>elit, sed do eiusmod tempor<br>incididunt ut <span class="more">learn more...</span></p></div>
  <div class="abs svc-col" style="left:352px;top:86px;width:140px"><h3 style="font-size:12.5px">CHECK UP</h3><p style="font-size:8.3px;line-height:17.5px;margin-top:2px">Lorem ipsum dolor sit<br>amet, consectetur adipiscing<br>elit, sed do eiusmod tempor<br>incididunt ut <span class="more">learn more...</span></p></div>
</section>

<h2 class="abs title" style="left:201px;width:200px;top:894px;font-size:17px">GET IN TOUCH</h2>
<div class="abs portrait" style="left:112px;top:938px;width:132px;height:132px" role="img" aria-label="Portrait photo of the clinician"></div>
<div class="abs field" style="left:258px;top:941px;width:248px;height:23px;font-size:12px;padding:4px 0 0 17px">NAME *</div>
<div class="abs field" style="left:258px;top:967px;width:248px;height:23px;font-size:12px;padding:4px 0 0 17px">EMAIL *</div>
<div class="abs field" style="left:258px;top:993px;width:248px;height:22px;font-size:12px;padding:4px 0 0 17px">PHONE NUMBER *</div>
<div class="abs field" style="left:258px;top:1018px;width:248px;height:50px;font-size:12px;padding:4px 0 0 17px">MESSAGE *</div>
<div class="abs btn btn-solid" style="left:431px;top:1077px;width:75px;height:25px;font-size:8px">SEND</div>
<p class="abs info" style="left:115px;top:1130px;font-size:12.5px;line-height:21px">#4/7 Linden Quay<br>Road, PH 55018,<br>Harbor Bus Stop</p>
<p class="abs info" style="left:369px;top:1130px;font-size:12.5px;line-height:21px"><span class="label">PHONE</span><br>08104417260<br><span class="label">GENERAL ENQUIRIES</span><br>hello@brimwellharbor.com</p>

<div class="abs page-white" style="left:569px;top:0;width:631px;height:954px"></div>
<div class="abs btn btn-solid" style="left:758px;top:-4px;width:97px;height:30px;font-size:12px">CONTACT US</div>
<div class="abs btn btn-line" style="left:886px;top:-4px;width:97px;height:30px;font-size:12px">LEARN MORE</div>

<section class="abs services" style="left:569px;top:75px;width:631px;height:372px" role="img" aria-label="Coastal bay photo with islands and a sandy shore">
  <h2 class="abs svc-title" style="left:0;width:100%;top:68px;font-size:25px;font-weight:400">SERVICES</h2>
  <div class="abs svc-col" style="left:29px;top:116px;width:190px"><h3 style="font-size:18px">SPEAKING</h3><p style="font-size:12px;line-height:23px;margin-top:2px">Lorem ipsum dolor sit<br>amet, consectetur adipiscing<br>elit, sed do eiusmod tempor<br>incididunt ut &nbsp;<span class="more">learn more...</span></p></div>
  <div class="abs svc-col" style="left:225px;top:116px;width:190px"><h3 style="font-size:18px">TRAINING</h3><p style="font-size:12px;line-height:23px;margin-top:2px">Lorem ipsum dolor sit<br>amet, consectetur adipiscing<br>elit, sed do eiusmod tempor<br>incididunt ut &nbsp;<span class="more">learn more...</span></p></div>
  <div class="abs svc-col" style="left:421px;top:116px;width:190px"><h3 style="font-size:18px">CHECK UP</h3><p style="font-size:12px;line-height:23px;margin-top:2px">Lorem ipsum dolor sit<br>amet, consectetur adipiscing<br>elit, sed do eiusmod tempor<br>incididunt ut &nbsp;<span class="more">learn more...</span></p></div>
</section>

<h2 class="abs title" style="left:712px;width:300px;top:504px;font-size:24px">GET IN TOUCH</h2>
<div class="abs portrait" style="left:610px;top:565px;width:174px;height:174px;border-width:5px" role="img" aria-label="Portrait photo of the clinician"></div>
<div class="abs field" style="left:806px;top:568px;width:328px;height:30px;font-size:17px;padding:5px 0 0 23px">NAME *</div>
<div class="abs field" style="left:806px;top:602px;width:328px;height:31px;font-size:17px;padding:5px 0 0 23px">EMAIL *</div>
<div class="abs field" style="left:806px;top:637px;width:328px;height:30px;font-size:17px;padding:5px 0 0 23px">PHONE NUMBER *</div>
<div class="abs field" style="left:806px;top:672px;width:328px;height:65px;font-size:17px;padding:5px 0 0 23px">MESSAGE *</div>
<div class="abs btn btn-solid" style="left:1035px;top:749px;width:98px;height:33px;font-size:12px">SEND</div>
<p class="abs info" style="left:614px;top:817px;font-size:17px;line-height:28px">#4/7 Linden Quay<br>Road, PH 55018,<br>Harbor Bus Stop</p>
<p class="abs info" style="left:952px;top:817px;font-size:17px;line-height:28px"><span class="label">PHONE</span><br>08104417260<br><span class="label">GENERAL ENQUIRIES</span><br>hello@brimwellharbor.com</p>

<div class="abs newsletter">
  <div class="abs" style="left:55px;top:29px;font-size:11px">Subscribe to our newsletter</div>
  <div class="abs" style="left:220px;top:20px;width:234px;height:30px;background:#fff;color:var(--cyan);font-size:11px;padding:9px 0 0 23px">hello@brimwellharbor.com</div>
  <div class="abs" style="left:454px;top:20px;width:94px;height:30px;background:var(--cyan);color:#fff;font-size:11px;display:flex;align-items:center;justify-content:center">SEND</div>
</div>
<footer class="abs footer">
  <div class="abs" style="left:45px;top:18px">© 2018 Brimwell Harbor</div>
  <div class="abs" style="left:445px;top:18px;font-size:9px">Terms</div>
  <div class="abs" style="left:482px;top:18px;font-size:9px">Privacy</div>
  <div class="abs social" style="left:524px;top:14px" aria-label="Social link"></div>
  <div class="abs social" style="left:554px;top:14px;background:#3fa7e0" aria-label="Social link"></div>
  <div class="abs social" style="left:584px;top:14px;background:#1f7bc2" aria-label="Social link"></div>
</footer>
<div class="abs backdrop-low" role="img" aria-label="Blurred coastal photograph"></div>

</body>
</html>
```